Visitenkarten-Design für Ferienhausvermietung
Zielgruppe
Vermietung eines Ferienhauses
Aufgabenstellung
Die Visitenkarte sollte edel und hochwertig wirken...
Es wäre mir wichtig, dass die Visitenkarte im Querformat erstellt wird.
Die Farben vom Logo lauten:
green: C = 43 M = 0 Y = 100 N = 16
brown: C = 39 M = 57 J = 87 N = 53
sky blue: C = 14 M = 6 J = 6 N = 0
Aber bitte nicht so viel in den Visitenkarten verwenden. Die Visitenkarten sollen eher neutral gehalten werden.
Die Schriften
font
Lindmark : Satisfaction
Ferienhaus : Corbert Regular
Flyer-Design für Ferienhausvermietung Flyer-Design für Ferienhausvermietung"
Es soll ein Flyer im Format DIN A4 erstellt werden. Der beidseitig bedruckt wird und dann 6seitig gefaltet wird. Ich benötige für den Flyer: Beschreibung/Ausstattung des Ferienhauses Beschreibung der Lage Beschreibung der Umgebung Anfahrt/Lage/Kontakt
Logo-Design für Ferienhaus ´Sa Verna´auf Mallorca mit eigenem Tennisplatz und Pool Logo-Design für Ferienhaus ´Sa Verna´auf Mallorca mit eigenem Tennisplatz und Pool"
Sie können sich meine Finca auf der Website: Casoveria anschauen. Ort: Costitx Name des Hauses: Finca Morell (heißt nur auf der Website so). Der Name am Tor Haus: Finca Sa Verna. Ich mag es gerne klassisch
Logo-Design für ein Feriendorf an der Ostsee Logo-Design für ein Feriendorf an der Ostsee"
* Nicht zu bunt, nicht zu verspielt, möglichst klar und aufgeräumt * In 2D, keine Schattierungen, keine Fotos im Hintergrund o. ä.. * Das Logo muss in allen Medien gut darstellbar sein! * Es sollte modern wirken, dennoch fröhlich, warm und einladend * Der Strand-/Wasserbezug muss deutlich we..
Flyer-Design für Ferienhaus Flyer-Design für Ferienhaus"
Flyerdesign für Ferienhaus: Din-Lang 2x gefalzt (übliche Format), 3 Seiten vorne und hinten.  Es sollte nach Möglichkeit an unsere Webseite (www.ferienhaus-kormoran-wendstrand.de) angepasst werden, druckfertig sein und per PDF auf unserer Webseite zum Downloaden integriert werden können. Meh..
Logo-Design für Ferienhaus Logo-Design für Ferienhaus"
Wir suchen ein Moderenes Design gern berücksichtig in Kombination mit dem Nationalpark Elmtal Kreuzwald. Da das Ferienhaus sich dort befindet.

```html
<!DOCTYPE html>
<html lang="de">
<head>
<meta charset="utf-8">
<title>Lindmark Ferienhaus – Visitenkarte</title>
<link rel="stylesheet" href="https://fonts.googleapis.com/css2?family=Great+Vibes&family=Barlow:wght@400;500&display=swap">
<style>
  :root {
    --page: #f4f2ef;
    --paper: #ffffff;
    --frame-brown: #3e2713;
    --logo-brown: #5a3a1f;
    --ink: #1e1e1e;
    --haze-beige: #d9d0c6;
    --haze-green: #dfeccb;
  }
  html, body {
    margin: 0;
    padding: 0;
    width: 786px;
    height: 1200px;
    overflow: hidden;
    background: var(--page);
  }
  .card {
    position: absolute;
    left: 23px;
    top: 360px;
    width: 740px;
    height: 480px;
    box-sizing: border-box;
    background: var(--paper);
    border: 4px solid var(--frame-brown);
    border-radius: 18px;
    overflow: hidden;
  }
  .backdrop-scene {
    position: absolute;
    left: 0;
    right: 0;
    bottom: 0;
    height: 190px;
    background:
      linear-gradient(180deg, rgba(255,255,255,1) 0%, rgba(255,255,255,0) 40%),
      linear-gradient(90deg, var(--haze-green) 0%, var(--haze-beige) 25%, var(--haze-beige) 75%, var(--haze-green) 100%);
    opacity: 0.5;
  }
  .brand {
    position: absolute;
    left: 40px;
    top: 106px;
    width: 260px;
    height: 260px;
  }
  .brand-mark {
    position: absolute;
    inset: 0;
    width: 260px;
    height: 260px;
  }
  .brand-name {
    position: absolute;
    left: 0;
    right: 0;
    top: 50%;
    margin: 0;
    transform: translateY(-50%);
    text-align: center;
    font-family: "Barlow", sans-serif;
    font-weight: 500;
    font-size: 42px;
    line-height: 1;
    color: var(--logo-brown);
  }
  .details {
    position: absolute;
    left: 320px;
    right: 20px;
    top: 0;
    bottom: 0;
    text-align: center;
  }
  .owner-name {
    position: absolute;
    left: 0;
    right: 0;
    top: 48px;
    margin: 0;
    font-family: "Great Vibes", cursive;
    font-weight: 400;
    font-size: 60px;
    line-height: 1.15;
    color: var(--ink);
  }
  .contact {
    position: absolute;
    left: 0;
    right: 0;
    margin: 0;
    font-family: "Barlow", sans-serif;
    font-weight: 400;
    font-style: normal;
    font-size: 27px;
    line-height: 36px;
    color: var(--ink);
  }
  .contact-address { top: 168px; }
  .contact-lines { top: 270px; }
</style>
</head>
<body>
  <main class="card">
    <div class="backdrop-scene" role="img" aria-label="Zarte, verblasste Hintergrundfläche mit Ferienhaus und Bäumen"></div>

    <div class="brand">
      <svg class="brand-mark" viewBox="0 0 260 260" aria-hidden="true">
        <circle cx="130" cy="130" r="127" fill="none" stroke="var(--logo-brown)" stroke-width="4"/>
      </svg>
      <p class="brand-name">Lindmark</p>
    </div>

    <section class="details">
      <h1 class="owner-name">Max Mustermann</h1>
      <address class="contact contact-address">
        Mustermannstr. 123<br>
        98765 Musterstadt
      </address>
      <address class="contact contact-lines">
        0123 / 456 789 0<br>
        info@webseite.de<br>
        www.webseite.de
      </address>
    </section>
  </main>
</body>
</html>
```